Coastal Rubdown Oil Co. needs a new label.

This massage oil has been in Australia for over 20 years and needs a new label for its plastic 250ml bottles. The current label (8cm x 8cm) looks old fashioned and so we are looking for something that reflects freedom, relaxation, inspiration. The product is made from sweet almond oil and has different essential oils used to give unique smells. I have seen some lovely abstract vector images. I think we need a clean straight look with bright colours. There are currently six variations to the product. "Calm and Quiet Heads, Achy and Weary Limbs, Sweethearts Mix, Jasmine Soak Oil, Unwind Mixture, Up-Lifting Mixture" Different coloured labels have been used for each of the blends. I have included photos of existing bottles plus some ideas for the labels.

I would like to use the same font on the name of the brand Quorby Meadow. If we change the font it may be difficult for existing customers to find our product.

Also just under the name Quorby Meadow I would like to insert a type of logo (can be the shape of a tear drop or round circle) to say:

Massage Oil
Since 1970

The size of the label is 8cm x 12 cm for the front and the same size for the back of the label.
Updates

Coastal Rubdown oil Company has posted on the brief some images from Pixmarket plus two photos of the original bottles. I am looking for a new design which is bright in colour, fun and funky. I am not thinking along the lines of the traditional Herb and trees look. I think the original label is too busy and the colours overpower the label. The other point I think that is important is that the product has been around since 1970. If there is room I think a round logo which says: Massage Oil Since 1970 I am hoping that we can fit this information on the label Looking forward to seeing all the designs come thru. So far I have only had two designs come thru. Speak soon from hot sunny Australia. delia

Thank you to everyone who has already posted designs for our Massage Label. I have now edited the brief to include some more ideas on how to make this design the Best! I will email back to you straight away ideas and thoughts on your designs. Remember I live in Australia and can be either 10hrs in front or behind your time.

Project Deadline Extended
Reason: Due to busy lives and commitments over the next few days I feel that an extension will benefit all involved. Thank you to everyone who has submitted designs and working with me to create something beautiful. delia

Hello from Australia all the designers who have submitted some wonderful designs over the past two weeks. We are now entering the final three days of the competition. Thank you to everyone who has worked so hard to try and create the perfect label for my massage oil bottle. All of you have done a fantastic job. This has made the decision hard to make. Thank you to everyone. Please submit all your last minute designs soon. kind regards delia Australia

Target Market(s)

The type of person purchasing a massage oil blend will buy from a health food shop, pharmacy or from an on-line store. I believe they are wanting something bright that clearly communicates that that it is a massage oil.

Industry/Entity Type

Massage

Font styles to use
Script

Requirements
Must have
• Different colour for each massage oil blend.
Need same font for the name Quorby Meadow. (script font or similar)

Abstract design please.
Nice to have
• A logo under the name Quorby Meadow

Tear Drop or circle design that says:

Massage Oil
Since 1970

also we would like an outline for the back label. (see photo attached)

BACK LABEL information

A unique blend of essential oils in a fine light base.

Contains:

vegetable oil extract of nettle, sweet almond oil, ethanol, essential oils of lavender, lemongrass, orange & ylang ylang and vitamin E.

How to Use:

Shake well warm bottle in warm water if very cold.
Lovingly massage the body from head to toe.
Not for medicinal use.

Quorby Meadow
Pellow WA 6143
Phone: (08) 9472 1538

(LEAVE ROOM FOR BARCODE)
Should not have
• Too busy design or old fashioned design.
No dull colours.

```html
<!DOCTYPE html>
<html lang="en">
<head>
<meta charset="utf-8">
<title>Quorby Meadow – Massage Oil Labels</title>
<link rel="stylesheet" href="https://fonts.googleapis.com/css2?family=Pinyon+Script&family=Arimo&family=Caladea&display=swap">
<style>
  :root {
    --page: #ffffff;
    --band: #1b1b1b;
    --ink: #ffffff;
    --drop-light: #ffc43d;
    --drop-deep: #ff9a1f;
    --blend-bodies: #ffaa73;
    --blend-heads: #fddc6b;
    --blend-sweethearts: #ff4646;
    --blend-jasmine: #e6c3ff;
    --blend-unwind: #b1ffff;
    --blend-uplift: #acdf4a;
  }
  * { margin: 0; padding: 0; box-sizing: border-box; }
  html, body { width: 1200px; height: 806px; overflow: hidden; background: var(--page); }
  .sheet { position: relative; width: 1200px; height: 806px; }

  .label {
    position: absolute;
    width: 236px;
    height: 354px;
    background: var(--blend);
    overflow: hidden;
  }
  .label--bodies { left: 108px; top: 33px; --blend: var(--blend-bodies); }
  .label--heads { left: 359px; top: 33px; --blend: var(--blend-heads); }
  .label--sweethearts { left: 610px; top: 33px; --blend: var(--blend-sweethearts); }
  .label--jasmine { left: 861px; top: 33px; --blend: var(--blend-jasmine); }
  .label--unwind { left: 359px; top: 419px; --blend: var(--blend-unwind); }
  .label--uplift { left: 610px; top: 419px; --blend: var(--blend-uplift); }

  .label__band {
    position: absolute;
    left: 60px;
    top: 0;
    width: 116px;
    height: 100%;
    background: var(--band);
  }
  .label__backdrop {
    position: absolute;
    left: 0;
    top: 60px;
    width: 100%;
    height: 294px;
    background: linear-gradient(180deg, rgba(255,255,255,0) 0%, rgba(200,200,200,0.28) 40%, rgba(150,150,150,0.22) 100%);
  }
  .label__brand {
    position: absolute;
    left: 60px;
    top: 22px;
    width: 116px;
    text-align: center;
    font-family: "Pinyon Script", cursive;
    font-size: 30px;
    line-height: 28px;
    color: var(--ink);
  }
  .label__brand span { display: block; }
  .label__drop {
    position: absolute;
    left: 86px;
    top: 95px;
    width: 64px;
    height: 116px;
    border-radius: 32px 32px 32px 32px / 60px 60px 32px 32px;
    background: linear-gradient(160deg, var(--drop-light), var(--drop-deep));
  }
  .label__name {
    position: absolute;
    left: 50px;
    top: 219px;
    width: 136px;
    text-align: center;
    font-family: "Arimo", Arial, sans-serif;
    font-size: 18px;
    line-height: 21px;
    color: var(--ink);
  }
  .label__name span { display: block; }
  .label__details {
    position: absolute;
    left: 60px;
    top: 296px;
    width: 116px;
    text-align: center;
    font-family: "Caladea", Georgia, serif;
    font-size: 8.5px;
    line-height: 11.5px;
    color: var(--ink);
  }
  .label__details span { display: block; }
</style>
</head>
<body>
<main class="sheet">

  <section class="label label--bodies">
    <div class="label__backdrop" role="img" aria-label="Large faint oil drop backdrop"></div>
    <div class="label__band"></div>
    <h2 class="label__brand"><span>Quorby</span><span>Meadow</span></h2>
    <div class="label__drop" role="img" aria-label="Golden oil drop with flowing wave pattern"></div>
    <p class="label__name"><span>Achy &amp; Weary</span><span>Limbs</span></p>
    <p class="label__details"><span>Massage Oil</span><span>Since 1970</span><span>250ml</span></p>
  </section>

  <section class="label label--heads">
    <div class="label__backdrop" role="img" aria-label="Large faint oil drop backdrop"></div>
    <div class="label__band"></div>
    <h2 class="label__brand"><span>Quorby</span><span>Meadow</span></h2>
    <div class="label__drop" role="img" aria-label="Golden oil drop with flowing wave pattern"></div>
    <p class="label__name"><span>Calm &amp; Quiet</span><span>Heads</span></p>
    <p class="label__details"><span>Massage Oil</span><span>Since 1970</span><span>250ml</span></p>
  </section>

  <section class="label label--sweethearts">
    <div class="label__backdrop" role="img" aria-label="Large faint oil drop backdrop"></div>
    <div class="label__band"></div>
    <h2 class="label__brand"><span>Quorby</span><span>Meadow</span></h2>
    <div class="label__drop" role="img" aria-label="Golden oil drop with flowing wave pattern"></div>
    <p class="label__name"><span>Sweethearts</span><span>Mix</span></p>
    <p class="label__details"><span>Massage Oil</span><span>Since 1970</span><span>250ml</span></p>
  </section>

  <section class="label label--jasmine">
    <div class="label__backdrop" role="img" aria-label="Large faint oil drop backdrop"></div>
    <div class="label__band"></div>
    <h2 class="label__brand"><span>Quorby</span><span>Meadow</span></h2>
    <div class="label__drop" role="img" aria-label="Golden oil drop with flowing wave pattern"></div>
    <p class="label__name"><span>Jasmine</span><span>Soak Oil</span></p>
    <p class="label__details"><span>Massage Oil</span><span>Since 1970</span><span>250ml</span></p>
  </section>

  <section class="label label--unwind">
    <div class="label__backdrop" role="img" aria-label="Large faint oil drop backdrop"></div>
    <div class="label__band"></div>
    <h2 class="label__brand"><span>Quorby</span><span>Meadow</span></h2>
    <div class="label__drop" role="img" aria-label="Golden oil drop with flowing wave pattern"></div>
    <p class="label__name"><span>Unwind</span><span>Mixture</span></p>
    <p class="label__details"><span>Massage Oil</span><span>Since 1970</span><span>250ml</span></p>
  </section>

  <section class="label label--uplift">
    <div class="label__backdrop" role="img" aria-label="Large faint oil drop backdrop"></div>
    <div class="label__band"></div>
    <h2 class="label__brand"><span>Quorby</span><span>Meadow</span></h2>
    <div class="label__drop" role="img" aria-label="Golden oil drop with flowing wave pattern"></div>
    <p class="label__name"><span>Up-Lifting</span><span>Mixture</span></p>
    <p class="label__details"><span>Massage Oil</span><span>Since 1970</span><span>250ml</span></p>
  </section>

</main>
</body>
</html>
```